Brisco Energy PowerPoint Design

Looking for a sleek PowerPoint design for our energy services company. We supply EV charging, Solar, Battery Storage and more.

Please make the background white with hints of gray and utilize the exact dark blue and light blue colors in the logo.

This design should be sharp with minimal round edges.

Colors

Designer to choose colors to be used in the design.

```html
<!DOCTYPE html>
<html lang="en">
<head>
<meta charset="utf-8">
<title>Brisco Energy Presentation</title>
<link href="https://fonts.googleapis.com/css2?family=Outfit:wght@400;600;700;800&family=Montserrat:wght@400;500;600&display=swap" rel="stylesheet">
<style>
:root{
  --navy:#140d56;
  --blue:#3aaefc;
  --canvas:#86878b;
  --white:#ffffff;
  --ink:#1d1d2b;
  --muted:#3a3a48;
}
*{box-sizing:border-box;margin:0;padding:0}
html,body{width:982px;height:1200px;overflow:hidden}
body{background:var(--canvas);position:relative;font-family:"Montserrat",sans-serif;color:var(--ink)}
.slide{position:absolute;width:450px;height:253px;overflow:hidden;background:var(--white)}
.s1{left:31px;top:45px}.s2{left:501px;top:45px}
.s3{left:31px;top:325px}.s4{left:501px;top:325px}
.s5{left:31px;top:606px}.s6{left:501px;top:606px}
.s7{left:31px;top:896px}.s8{left:501px;top:896px}
.abs{position:absolute}
.photo{position:absolute}
.brand{position:absolute;display:flex;align-items:center;gap:3px;font-family:"Outfit",sans-serif;font-weight:700;color:var(--navy);font-size:9.5px;line-height:1.02;letter-spacing:.2px;white-space:nowrap}
.brand .mark{width:8px;height:8px;background:var(--blue);flex:none}
.brand.light{color:var(--white)}
.title{position:absolute;font-family:"Outfit",sans-serif;font-weight:800;color:var(--navy);font-size:14.5px;line-height:1.1}
.subtitle{position:absolute;font-size:7px;color:var(--ink)}
.body{font-size:7px;line-height:1.55;color:var(--muted)}

.cover-photo{inset:0;background:linear-gradient(180deg,#5c6a4a 0%,#4b5a3b 45%,#6f7370 62%,#3d3f42 100%)}
.cover-shade{position:absolute;inset:0;background:linear-gradient(180deg,rgba(20,20,30,.45),rgba(20,20,30,0) 55%)}
.cover-title{position:absolute;left:124px;top:18px;font-family:"Outfit",sans-serif;font-weight:800;font-size:16.5px;line-height:1.12;color:var(--white);letter-spacing:.4px}
.cover-rule{position:absolute;left:288px;top:23px;width:1.5px;height:72px;background:var(--white)}
.cover-info{position:absolute;left:305px;top:21px;color:var(--white);font-family:"Outfit",sans-serif;font-size:9.5px;line-height:1.2}
.cover-info p{margin-bottom:9px}

.about-list{position:absolute;left:16px;top:140px;width:190px;list-style:none}
.about-list li{position:relative;background:linear-gradient(90deg,#dff0fe 0 5px,transparent 5px);padding:3px 0 3px 18px;margin-bottom:3px;font-size:6.8px;line-height:1.35;min-height:16px;display:flex;align-items:center}
.about-list li::before{content:"";position:absolute;left:8px;top:50%;width:5px;height:5px;margin-top:-2.5px;border-radius:50%;background:var(--navy)}

.card{position:absolute;top:75px;width:101px;height:163px;border:2px solid var(--navy);background:var(--white);padding:14px 10px 0 10px}
.card .icon{width:30px;height:30px;background:var(--blue);margin-bottom:13px}
.card h3{font-family:"Outfit",sans-serif;font-weight:700;font-size:8px;line-height:1.25;color:var(--navy);margin-bottom:8px}
.card p{font-size:5.2px;line-height:1.45;color:var(--muted)}

.step{position:absolute;width:92px;text-align:center}
.step h3{font-family:"Outfit",sans-serif;font-weight:700;font-size:8px;color:var(--navy);margin-bottom:4px}
.step p{font-size:5.3px;line-height:1.5;color:var(--muted)}

.sol-text{position:absolute;left:267px;top:54px;width:162px;font-size:5.55px;line-height:9.85px;color:var(--muted);height:187px;overflow:hidden}

.sus-box{position:absolute;left:20px;top:131px;width:230px;height:111px;background:var(--blue);padding:10px 8px;list-style:none}
.sus-box li{color:var(--white);font-size:6.2px;line-height:12.9px;padding-left:7px;position:relative;white-space:nowrap}
.sus-box li::before{content:"";position:absolute;left:0;top:4.5px;border-left:3px solid var(--white);border-top:2px solid transparent;border-bottom:2px solid transparent}

.thanks-bg{inset:0;background:linear-gradient(135deg,#1a0f6e 0%,#2416a6 55%,#1a0f7a 100%)}
.thanks-center{position:absolute;left:0;right:0;text-align:center;color:var(--white)}
.thanks-rule{position:absolute;left:204px;width:42px;height:1.5px;background:var(--white)}
.thanks-title{font-family:"Outfit",sans-serif;font-weight:800;font-size:31px;letter-spacing:.5px}
.contact{position:absolute;top:218px;left:0;right:0;display:flex;justify-content:center;gap:16px;color:var(--white);font-size:8.5px;align-items:center}
.contact span{display:flex;align-items:center;gap:5px}
</style>
</head>
<body>

<section class="slide s1">
  <div class="photo cover-photo" role="img" aria-label="White electric car plugged into a charging station in front of trees"></div>
  <div class="cover-shade"></div>
  <div class="brand light" style="left:20px;top:30px;font-size:17px;gap:6px"><span class="mark" style="width:13px;height:13px"></span><span>BRISCO<br>ENERGY</span></div>
  <h1 class="cover-title">EMPOWERING A<br>SUSTAINABLE<br>FUTURE</h1>
  <div class="cover-rule"></div>
  <div class="cover-info">
    <p>Leaders in EV Charging,<br>Solar Energy, and Battery<br>Storage Solutions</p>
    <p>+1 555 010 2040</p>
    <p>info@briscoenergy.com</p>
  </div>
</section>

<section class="slide s2">
  <svg class="abs" style="inset:0" width="450" height="253" viewBox="0 0 450 253">
    <polygon points="240,0 450,0 450,253 217,253" fill="#3aaefc"/>
  </svg>
  <div class="photo" role="img" aria-label="Two workers in hard hats installing a solar panel on a roof" style="inset:0;clip-path:polygon(249px 0,450px 0,450px 253px,226px 253px);background:linear-gradient(160deg,#8fb6d6 0%,#3e5f86 45%,#1d2f52 100%)"></div>
  <div class="brand" style="left:14px;top:18px"><span class="mark"></span><span>BRISCO<br>ENERGY</span></div>
  <h2 class="title" style="left:80px;top:12px">About<br>Brisco Energy</h2>
  <p class="body abs" style="left:17px;top:74px;width:184px">Lorem ipsum dolor sit amet, con sectetur adipiscing elit, sed do eiusmod tempor incididunt ut labore et dolore magna aliqua. Quis ipsum suspendisse ultrices gravida. Risus commodo viverra maecenas accumsan lacus vel facilisis.</p>
  <ul class="about-list">
    <li>Established expertise in energy services</li>
    <li>Committed to sustainability and innovation</li>
    <li>Partnering with businesses, communities, and individuals to power the future</li>
    <li>Proven track record in EV charging, solar energy systems, and advanced battery storage</li>
  </ul>
</section>

<section class="slide s3">
  <svg class="abs" style="inset:0" width="450" height="253" viewBox="0 0 450 253">
    <polygon points="272,0 450,0 450,120 342,80" fill="#3aaefc"/>
    <polygon points="282,0 450,0 450,116 346,78" fill="#140d56"/>
  </svg>
  <div class="brand" style="left:14px;top:20px"><span class="mark"></span><span>BRISCO<br>ENERGY</span></div>
  <h2 class="title" style="left:83px;top:17px">Our Services</h2>
  <p class="subtitle" style="left:83px;top:38px">Lorem ipsum dolor sit amet, con sectetur adipiscing elit</p>
  <div class="card" style="left:14px"><div class="icon"></div><h3>EV Charging<br>Solutions</h3><p>Lorem ipsum dolor sit amet, con sectetur adipiscing elit, sed do eiusmod tempor incididunt ut labore et dolore magna aliqua. Quis ipsum suspendisse ultrices grav ida. Risus commodo viverra maecenas accu.</p></div>
  <div class="card" style="left:125px"><div class="icon"></div><h3>Solar Energy<br>Systems</h3><p>Lorem ipsum dolor sit amet, con sectetur adipiscing elit, sed do eiusmod tempor incididunt ut labore et dolore magna aliqua. Quis ipsum suspendisse ultrices grav ida. Risus commodo viverra maecenas accu.</p></div>
  <div class="card" style="left:233px"><div class="icon"></div><h3>Battery<br>Storage</h3><p>Lorem ipsum dolor sit amet, con sectetur adipiscing elit, sed do eiusmod tempor incididunt ut labore et dolore magna aliqua. Quis ipsum suspendisse ultrices grav ida. Risus commodo viverra maecenas accu.</p></div>
  <div class="card" style="left:339px"><div class="icon"></div><h3>Energy<br>Consultancy</h3><p>Lorem ipsum dolor sit amet, con sectetur adipiscing elit, sed do eiusmod tempor incididunt ut labore et dolore magna aliqua. Quis ipsum suspendisse ultrices grav ida. Risus commodo viverra maecenas accu.</p></div>
</section>

<section class="slide s4">
  <div class="brand" style="left:20px;top:18px"><span class="mark"></span><span>BRISCO<br>ENERGY</span></div>
  <h2 class="title" style="left:90px;top:15px">How It Works</h2>
  <p class="subtitle" style="left:90px;top:37px">Lorem ipsum dolor sit amet, con sectetur adipiscing elit</p>
  <svg class="abs" style="left:0;top:0" width="450" height="253" viewBox="0 0 450 253" fill="none" stroke="#140d56" stroke-width="0.8">
    <path d="M14 108 H36 A40 40 0 0 1 111 100"/>
    <path d="M116 114 H134 A40 40 0 0 0 215 114"/>
    <path d="M215 108 H236 A40 40 0 0 1 316 108"/>
    <path d="M316 115 H338 A40 40 0 0 0 419 115 H437"/>
    <path d="M111 100 V108 H116 V114"/>
    <g fill="#140d56" stroke="none">
      <circle cx="14" cy="108" r="2"/><circle cx="116" cy="114" r="2"/><circle cx="134" cy="114" r="2"/>
      <circle cx="215" cy="108" r="2"/><circle cx="233" cy="114" r="2"/><circle cx="316" cy="115" r="2"/>
      <circle cx="338" cy="115" r="2"/><circle cx="437" cy="115" r="2"/>
    </g>
    <circle cx="73.5" cy="108" r="32" fill="#140d56" stroke="none"/>
    <circle cx="175" cy="115" r="32" fill="#3aaefc" stroke="none"/>
    <circle cx="276" cy="108" r="32" fill="#140d56" stroke="none"/>
    <circle cx="379" cy="115" r="32" fill="#3aaefc" stroke="none"/>
    <g stroke="#ffffff" stroke-width="1.6">
      <path d="M70 96 h10 v10 h-10 z M72 92 v4 M78 92 v4 M75 106 v4 q0 8 -8 8 q-6 0 -6 -5"/>
      <circle cx="170" cy="118" r="4"/><path d="M163 129 q7 -8 14 0"/><circle cx="181" cy="116" r="4"/><path d="M175 127 q6 -8 13 0"/>
      <rect x="265" y="100" width="22" height="16"/><path d="M272 100 v16 M280 100 v16 M268 96 h4 M280 96 h4"/>
      <rect x="368" y="106" width="22" height="13"/><path d="M368 110.5 h22 M368 115 h22 M373.5 106 v13 M379 106 v13 M384.5 106 v13 M375 123 h8"/>
    </g>
  </svg>
  <div class="step" style="left:27px;top:150px"><h3>1. Lorem Ipsum</h3><p>Lorem ipsum dolor sit amet, consectetur adipiscing elit, sed do eiusmod tempor incididunt ut labore et dolore magna aliqua. Ut enim ad minim veniam, quis nostrud exercitation</p></div>
  <div class="step" style="left:129px;top:172px"><h3>2. Lorem Ipsum</h3><p>Lorem ipsum dolor sit amet, consectetur adipiscing elit, sed do eiusmod tempor incididunt ut labore et dolore magna aliqua. Ut enim ad minim veniam, quis nostrud exercitation</p></div>
  <div class="step" style="left:230px;top:150px"><h3>3. Lorem Ipsum</h3><p>Lorem ipsum dolor sit amet, consectetur adipiscing elit, sed do eiusmod tempor incididunt ut labore et dolore magna aliqua. Ut enim ad minim veniam, quis nostrud exercitation</p></div>
  <div class="step" style="left:333px;top:172px"><h3>4. Lorem Ipsum</h3><p>Lorem ipsum dolor sit amet, consectetur adipiscing elit, sed do eiusmod tempor incididunt ut labore et dolore magna aliqua. Ut enim ad minim veniam, quis nostrud exercitation</p></div>
</section>

<section class="slide s5">
  <div class="brand" style="left:11px;top:15px"><span class="mark"></span><span>BRISCO<br>ENERGY</span></div>
  <h2 class="title" style="left:77px;top:13px">Solutions</h2>
  <p class="subtitle" style="left:77px;top:33px">Lorem ipsum dolor sit amet, con sectetur adipiscing elit</p>
  <div class="abs" style="left:8px;top:56.5px;width:241.5px;height:187.5px;background:var(--blue)"></div>
  <div class="photo" role="img" aria-label="Wall-mounted home battery units with glowing charge indicators" style="left:0;top:62px;width:241.5px;height:191px;background:linear-gradient(120deg,#3b3e44 0%,#8a8e94 45%,#cfd2d6 70%,#6e7278 100%)"></div>
  <p class="sol-text">Lorem ipsum dolor sit amet, con sectetur adipiscing elit, sed do eiusmod tempor incididunt ut labore et dolore magna aliqua. Quis ipsum suspendisse ultrices gravida. Risus commodo viverra maecenas accumsan lacus vel facilisis. Sed ut perspiciatis unde omnis iste natus error sit voluptatem accusantium doloremque laudantium, totam rem aperiam, eaque ipsa quae ab illo inventore veritatis et quasi architecto beatae vitae dicta sunt explicabo. Nemo enim ipsam voluptatem quia voluptas sit aspernatur aut odit aut fugit, sed quia consequuntur magni dolores eos qui ratione voluptatem sequi nesciunt. Neque porro quisquam est, qui dolorem ipsum quia dolor sit amet, consectetur, adipisci velit, sed quia non numquam eius modi tempora incidunt ut labore et dolore magnam aliquam quaerat voluptatem. Ut enim ad minima veniam, quis nostrum exercitationem ullam corporis suscipit laboriosam, nisi ut aliquid ex ea commodi consequatur? Quis autem vel eum iure reprehenderit qui in ea voluptate velit esse quam nihil molestiae consequatur, vel illum qui</p>
</section>

<section class="slide s6">
  <div class="brand" style="left:20px;top:15px"><span class="mark"></span><span>BRISCO<br>ENERGY</span></div>
  <h2 class="title" style="left:83px;top:17px">Profit</h2>
  <svg class="abs" style="left:0;top:0" width="450" height="253" viewBox="0 0 450 253" font-family="Montserrat, sans-serif" font-size="5.5" fill="#333">
    <g stroke="#777" stroke-width="0.5" stroke-dasharray="1.5 1.5">
      <line x1="35" y1="64" x2="425" y2="64"/><line x1="35" y1="90.5" x2="425" y2="90.5"/>
      <line x1="35" y1="117" x2="425" y2="117"/><line x1="35" y1="143.5" x2="425" y2="143.5"/>
      <line x1="35" y1="170" x2="425" y2="170"/><line x1="35" y1="196.5" x2="425" y2="196.5"/>
    </g>
    <line x1="35" y1="64" x2="35" y2="223" stroke="#222" stroke-width="0.6"/>
    <line x1="35" y1="223" x2="425" y2="223" stroke="#222" stroke-width="0.6"/>
    <g text-anchor="end">
      <text x="27" y="66">60</text><text x="27" y="92.5">50</text><text x="27" y="119">40</text>
      <text x="27" y="145.5">30</text><text x="27" y="172">20</text><text x="27" y="198.5">10</text><text x="27" y="225">0</text>
    </g>
    <rect x="40" y="162" width="15" height="61" fill="#2f5a8f"/>
    <rect x="74" y="127.6" width="15" height="95.4" fill="#f29f33"/>
    <rect x="108" y="185.9" width="15" height="37.1" fill="#85b043"/>
    <rect x="142" y="164.7" width="15" height="58.3" fill="#6f4f9a"/>
    <rect x="175" y="117" width="15" height="106" fill="#17998a"/>
    <rect x="208" y="74.6" width="15" height="148.4" fill="#8b2b2f"/>
    <rect x="242" y="148.8" width="15" height="74.2" fill="#3b9cc4"/>
    <rect x="274" y="196.5" width="15" height="26.5" fill="#8b2b2f"/>
    <rect x="308" y="143.5" width="15" height="79.5" fill="#85b043"/>
    <rect x="342" y="111.7" width="15" height="111.3" fill="#6f4f9a"/>
    <rect x="376" y="164.7" width="15" height="58.3" fill="#3b9cc4"/>
    <rect x="409" y="135.5" width="15" height="87.5" fill="#f29f33"/>
    <g text-anchor="middle" font-size="4.5">
      <text x="47.5" y="233">Jan</text><text x="81.5" y="233">Feb</text><text x="115.5" y="233">Mar</text>
      <text x="149.5" y="233">Apr</text><text x="182.5" y="233">May</text><text x="215.5" y="233">Jun</text>
      <text x="249.5" y="233">July</text><text x="281.5" y="233">Aug</text><text x="315.5" y="233">Sep</text>
      <text x="349.5" y="233">Oct</text><text x="383.5" y="233">Nov</text><text x="416.5" y="233">Dec</text>
    </g>
  </svg>
</section>

<section class="slide s7">
  <div class="brand" style="left:20px;top:17px"><span class="mark"></span><span>BRISCO<br>ENERGY</span></div>
  <h2 class="title" style="left:79px;top:13px">Sustainability<br>Commitment</h2>
  <h3 class="abs" style="left:20px;top:62px;font-family:'Outfit',sans-serif;font-weight:700;font-size:8.5px;color:var(--navy)">Lorem ipsum dolor sit amet consectetur</h3>
  <p class="body abs" style="left:19px;top:77px;width:235px;font-size:7px;line-height:1.55;color:var(--ink)">Lorem ipsum dolor sit amet, con sectetur adipiscing elit, sed do eiusmod tempor incididunt ut labore et dolore magna aliqua. Quis ipsum suspen disse ultrices gravida. Risus commodo viverra maecenas accumsan lacus vel facilisis.</p>
  <ul class="sus-box">
    <li>Lorem ipsum dolor sit amet, consectetur adipiscing elit.</li>
    <li>Mauris nec enim iaculis, vulputate ante vel, vestibulum arcu.</li>
    <li>Cras ut felis mollis, egestas neque quis, semper mauris.</li>
    <li>Fusce lobortis felis vel erat lacinia pellentesque.</li>
    <li>Praesent id purus et est iaculis dignissim.</li>
    <li>Nulla condimentum tellus quis felis dapibus</li>
    <li>Fusce pellentesque justo id eros</li>
  </ul>
  <div class="photo" role="img" aria-label="Rows of battery storage containers beside power line towers at sunset" style="left:274px;top:0;width:176px;height:253px;background:linear-gradient(180deg,#c9c7c2 0%,#e8b98a 30%,#6c7564 48%,#9fa3a6 62%,#d6d8da 100%)"></div>
</section>

<section class="slide s8">
  <div class="photo thanks-bg" role="img" aria-label="Deep blue close-up of solar panel cells"></div>
  <div class="thanks-center" style="top:28px;display:flex;justify-content:center">
    <div class="brand light" style="position:static;font-size:18px;gap:7px"><span class="mark" style="width:14px;height:14px"></span><span>BRISCO<br>ENERGY</span></div>
  </div>
  <div class="thanks-rule" style="top:112px"></div>
  <div class="thanks-center thanks-title" style="top:118px">THANK YOU</div>
  <div class="thanks-rule" style="top:169px"></div>
  <div class="contact">
    <span><svg width="7" height="7" viewBox="0 0 24 24" fill="#fff"><path d="M6.6 10.8a15 15 0 0 0 6.6 6.6l2.2-2.2c.3-.3.7-.4 1-.2 1.1.4 2.3.6 3.6.6.6 0 1 .4 1 1V20c0 .6-.4 1-1 1A17 17 0 0 1 3 4c0-.6.4-1 1-1h3.5c.6 0 1 .4 1 1 0 1.3.2 2.5.6 3.6.1.3 0 .7-.2 1z"/></svg>+1 555 010 2040</span>
    <span><svg width="7" height="6" viewBox="0 0 24 18" fill="#fff"><path d="M0 0h24v2L12 10 0 2z M0 5l12 8 12-8v13H0z"/></svg>info@briscoenergy.com</span>
  </div>
</section>

</body>
</html>
```